Skip Bin Hire Business

We are an existing business that hire out skip bins for domestic and commercial use. We are looking for a fresh look with no colours or designs in mind.
We have 2m3 and 3m3 skip bins and 3m3 up to 24m3 walk in bins.
Visit our website for more information.
www.harborcrate.com.au
We are going to add a photo of a 3m3 skip as this is a new product for our company and not available on our website at this stage.

Industry/Entity Type

Business

Contact Information for Business Card

Harbor Crate
9172-4086
www.harborcrate.com.au

```html
<!DOCTYPE html>
<html lang="en">
<head>
<meta charset="utf-8">
<title>Harbor Crate – Business Card</title>
<link rel="stylesheet" href="https://fonts.googleapis.com/css2?family=Open+Sans:wght@700;800&display=swap">
<style>
  :root {
    --page: #ffffff;
    --photo-light: #ececec;
    --photo-mid: #cdcdcd;
    --skip-tone-light: #e9dcb8;
    --skip-tone-deep: #e0b04a;
    --band-top: #f7c548;
    --band-bottom: #e4a421;
    --panel-dark: #2b2b2b;
    --panel-deep: #1c1c1c;
    --gold: #d99b2b;
    --logo-ink: #2a2a2a;
  }
  * { box-sizing: border-box; margin: 0; padding: 0; }
  html, body {
    width: 1200px;
    height: 900px;
    overflow: hidden;
    background: var(--page);
  }
  .canvas {
    position: relative;
    width: 1200px;
    height: 900px;
  }
  .card {
    position: absolute;
    left: 100px;
    top: 164px;
    width: 1000px;
    height: 572px;
    overflow: hidden;
    box-shadow: 0 14px 30px rgba(0,0,0,0.18);
    font-family: "Open Sans", Arial, sans-serif;
  }
  .card-header {
    position: absolute;
    left: 0; top: 0;
    width: 100%;
    height: 286px;
    background: var(--photo-light);
  }
  .yard-photo {
    position: absolute;
    left: 0; top: 0;
    width: 64%;
    height: 100%;
    background: linear-gradient(90deg, var(--photo-mid) 0%, #d9d9d9 60%, var(--photo-light) 100%);
  }
  .skip-photo {
    position: absolute;
    left: 64%;
    top: 0;
    width: 36%;
    height: 100%;
    background: linear-gradient(180deg, var(--skip-tone-light) 0%, var(--skip-tone-deep) 100%);
  }
  .brand-name {
    position: absolute;
    left: 90px;
    top: 46px;
    font-weight: 800;
    font-size: 96px;
    line-height: 0.98;
    color: var(--logo-ink);
  }
  .brand-name span { display: block; }
  .brand-name span + span { padding-left: 160px; }
  .accent-band {
    position: absolute;
    left: 0; top: 286px;
    width: 100%;
    height: 34px;
    background: linear-gradient(180deg, var(--band-top) 0%, var(--band-bottom) 100%);
  }
  .contact-panel {
    position: absolute;
    left: 0; top: 320px;
    width: 100%;
    height: 252px;
    background: linear-gradient(180deg, var(--panel-deep) 0%, var(--panel-dark) 60%, var(--panel-deep) 100%);
    display: flex;
    flex-direction: column;
    align-items: center;
    justify-content: center;
    padding-bottom: 20px;
    gap: 16px;
  }
  .contact-phone {
    font-weight: 700;
    font-size: 52px;
    color: var(--gold);
    line-height: 1.1;
  }
  .contact-web {
    font-weight: 700;
    font-size: 46px;
    color: var(--gold);
    line-height: 1.1;
  }
</style>
</head>
<body>
  <div class="canvas">
    <div class="card">
      <div class="card-header">
        <div class="yard-photo" role="img" aria-label="Black and white photo of a skip bin truck parked in a yard"></div>
        <div class="skip-photo" role="img" aria-label="Photo of a yellow 3m3 skip bin"></div>
        <h1 class="brand-name"><span>Harbor</span><span>Crate</span></h1>
      </div>
      <div class="accent-band"></div>
      <div class="contact-panel">
        <p class="contact-phone">(03)9172-4086</p>
        <p class="contact-web">www.harborcrate.com.au</p>
      </div>
    </div>
  </div>
</body>
</html>
```